Hal's Remedies Business Card Design Project

I need a business card designed for my pharmacy Hal's Remedies. I would like just the logo on one side, maybe with black background and white lettering. The other side I would also like to include my logo which is attached. Also, please include my name and the following information:
Hal Norwick Owner/Pharm D.
Business address is 7163 N Birch Rd Sioux Falls, SD 57291.
Phone number is 605-318-6027 and fax # is 605-318-6031.
my email address is hal@halsremedies.example.
My website is www.halsremedies.example.
My business hours are Monday-Friday 8am-7 pm. Saturday 8am-12 pm. Sunday Closed.
I would like the design to include my logo colors, black, white, and neon green. Silver may be added as a highlight. Thanks.
Pharmacy
See above in product description

```html
<!DOCTYPE html>
<html lang="en">
<head>
<meta charset="utf-8">
<title>Hal's Remedies – Business Card</title>
<link rel="stylesheet" href="https://fonts.googleapis.com/css2?family=Alegreya+Sans:wght@400;500&family=Open+Sans:wght@600&family=Tenor+Sans&display=swap">
<style>
  :root {
    --canvas: #e4e4e2;
    --card-dark: #262626;
    --card-light: #f7f7f7;
    --ink-dark: #3c3c3c;
    --ink-light: #eeeeee;
    --ink-muted: #bdbdbd;
    --neon: #9bd23c;
    --silver: #8c8c8c;
  }
  * { box-sizing: border-box; margin: 0; padding: 0; }
  html, body { width: 1200px; height: 1049px; overflow: hidden; }
  body {
    background: var(--canvas);
    font-family: "Alegreya Sans", sans-serif;
    position: relative;
  }
  .card {
    position: absolute;
    left: 250px;
    width: 700px;
    height: 400px;
    overflow: hidden;
    box-shadow: 0 6px 18px rgba(0,0,0,0.18);
  }
  .card--back { top: 90px; background: var(--card-dark); color: var(--ink-light); }
  .card--front { top: 560px; background: linear-gradient(160deg, #ffffff 0%, var(--card-light) 60%, #ececec 100%); color: var(--ink-dark); }

  /* Back */
  .hours {
    position: absolute; top: 34px; left: 40px; right: 40px;
    display: flex; justify-content: space-between; align-items: center;
    font-size: 15px; color: var(--ink-muted);
  }
  .hours__sep { width: 1px; height: 16px; background: var(--silver); }
  .brand {
    display: flex; align-items: center; gap: 14px;
    font-family: "Open Sans", sans-serif; font-weight: 600;
  }
  .brand__mark { width: 18px; height: 18px; background: var(--neon); }
  .card--back .brand {
    position: absolute; top: 160px; left: 0; right: 0; justify-content: center;
    font-size: 40px; color: var(--ink-light);
  }
  .website {
    position: absolute; top: 270px; left: 0; right: 0; text-align: center;
    font-size: 24px; letter-spacing: 0.5px; color: var(--ink-light);
  }
  .edge-bar { position: absolute; bottom: 0; left: 0; right: 0; height: 6px; display: flex; }
  .edge-bar__grey { width: 29%; background: var(--silver); }
  .edge-bar__neon { width: 31%; background: var(--neon); }
  .card--back .edge-bar__grey { background: #4a4a4a; }

  /* Front */
  .card--front .brand {
    position: absolute; top: 40px; left: 40px;
    font-size: 36px; color: var(--ink-dark);
  }
  .holder { position: absolute; top: 132px; left: 40px; }
  .holder__name {
    font-family: "Tenor Sans", sans-serif; font-size: 33px; line-height: 1;
    letter-spacing: 0.5px; color: var(--ink-dark);
  }
  .holder__surname { color: var(--neon); }
  .holder__title { font-size: 19px; margin-top: 2px; color: var(--ink-dark); }
  .contact {
    position: absolute; right: 40px; bottom: 42px; text-align: right;
    font-size: 20px; line-height: 1.2; color: var(--ink-dark);
    font-style: normal;
  }
</style>
</head>
<body>
  <section class="card card--back" aria-label="Card back">
    <div class="hours">
      <span>Monday-Friday 8am-7pm</span>
      <span class="hours__sep"></span>
      <span>Saturday 8am-12pm</span>
      <span class="hours__sep"></span>
      <span>Sunday Closed</span>
    </div>
    <div class="brand"><span class="brand__mark"></span><span>Hal's Remedies</span></div>
    <div class="website">www.halsremedies.example</div>
    <div class="edge-bar"><span class="edge-bar__grey"></span><span class="edge-bar__neon"></span></div>
  </section>

  <section class="card card--front" aria-label="Card front">
    <div class="brand"><span class="brand__mark"></span><span>Hal's Remedies</span></div>
    <div class="holder">
      <div class="holder__name">HAL<span class="holder__surname">NORWICK</span></div>
      <div class="holder__title">Owner/Pharm D.</div>
    </div>
    <address class="contact">
      7163 N Birch Rd Sioux Falls, SD 57291<br>
      phone: 605-318-6027 fax: 605-318-6031<br>
      hal@halsremedies.example<br>
      www.halsremedies.example
    </address>
    <div class="edge-bar"><span class="edge-bar__grey"></span><span class="edge-bar__neon"></span></div>
  </section>
</body>
</html>
```